Lumaray Vellardo needs your help to create a new identity design

We are a basketball team based in Crescentino, Italy.
The official club colors are royal blue and white.
Basically we need a new letterhead and envelope design but not necessary a new logo, but if you want to suggest us a new one we are glad to evaluate it.
If you need any other info please contact us.

Target Market(s)

athletes, their families, other clubs, public institutions, companies

Industry/Entity Type

Club

Font styles to use
Other font styles liked:
• the font of our logo or something very similar

Colors
0592cd
ffffff

Requirements
Must have
• our logo, attached to this request; address and other club info such as email address, phone number, facebook page, VAT lot and tax code and obviously our official club colors royal blue and white
Nice to have
• a clear, simple and quite minimal design. A watermark
Should not have
• any other graphic or images such as hoops, ball or court

```html
<!DOCTYPE html>
<html lang="en">
<head>
<meta charset="utf-8">
<title>Lumaray Vellardo – Letterhead</title>
<link href="https://fonts.googleapis.com/css2?family=Open+Sans:ital,wght@0,400;0,600;0,700;1,400&family=Saira+Semi+Condensed:wght@700&display=swap" rel="stylesheet">
<style>
  :root {
    --backdrop: #a9cdf0;
    --paper: #ffffff;
    --navy: #1d3a78;
    --royal: #2f5aa8;
    --sky: #0592cd;
    --grass: #6aa532;
    --ink: #3a3a3a;
    --muted: #6b6b6b;
    --dot: #e0483a;
    --faint: #eef1f4;
  }
  * { box-sizing: border-box; margin: 0; padding: 0; }
  html, body { width: 1200px; height: 784px; overflow: hidden; }
  body {
    background: var(--backdrop);
    font-family: "Open Sans", sans-serif;
    color: var(--ink);
    position: relative;
  }
  .letterhead {
    position: absolute;
    left: 340px; top: 22px;
    width: 520px; height: 740px;
    background: var(--paper);
    box-shadow: 0 6px 22px rgba(30, 70, 130, 0.25);
    overflow: hidden;
  }
  .club-mark {
    position: absolute; left: 34px; top: 28px;
    display: flex; align-items: center; gap: 8px;
    font-size: 11px; font-weight: 700; color: var(--navy);
  }
  .club-mark .disc {
    width: 40px; height: 40px; border-radius: 50%;
    background: var(--navy);
  }
  .club-details {
    position: absolute; right: 34px; top: 32px;
    text-align: right;
  }
  .club-details .club-name {
    font-family: "Saira Semi Condensed", sans-serif;
    font-weight: 700; font-size: 15px; letter-spacing: .3px;
    text-transform: uppercase; color: var(--navy);
  }
  .club-details .club-name span { color: var(--sky); }
  .club-details address {
    font-style: normal; font-size: 7.5px; line-height: 1.45; color: var(--muted);
  }
  .letter-body {
    position: absolute; left: 60px; top: 112px; width: 400px;
    font-size: 8.4px; line-height: 1.6; color: var(--ink);
  }
  .salutation {
    font-style: italic; font-size: 12px; margin-bottom: 12px; color: var(--ink);
  }
  .letter-body p { text-align: justify; margin-bottom: 10px; }
  .signature {
    display: block; width: 80px; height: 34px; margin-top: 18px;
    background: linear-gradient(90deg, #e6e6e6, #f4f4f4);
    border-radius: 4px;
  }
  .watermark {
    position: absolute; left: 170px; top: 440px;
    width: 220px; height: 220px; border-radius: 50%;
    background: var(--faint);
    display: flex; align-items: center; justify-content: center;
  }
  .watermark span {
    font-size: 22px; font-weight: 700; color: #dfe4ea; text-align: center; line-height: 1.15;
  }
  .contact-list {
    position: absolute; left: 34px; bottom: 34px;
    list-style: none; font-size: 7.5px; line-height: 1.75; color: var(--muted);
  }
  .contact-list li { display: flex; align-items: center; gap: 6px; }
  .contact-list li::before {
    content: ""; width: 5px; height: 5px; border-radius: 50%;
    background: var(--dot); flex: none;
  }
  .corner-swoosh {
    position: absolute; right: 0; bottom: 0; width: 520px; height: 740px;
  }
</style>
</head>
<body>
  <main class="letterhead">
    <svg class="corner-swoosh" viewBox="0 0 520 740" aria-hidden="true">
      <defs>
        <linearGradient id="royal-fade" x1="0" y1="1" x2="1" y2="0">
          <stop offset="0" stop-color="var(--navy)"/>
          <stop offset="1" stop-color="#5f86cc"/>
        </linearGradient>
      </defs>
      <path d="M250 740 L520 700 L520 740 Z" fill="var(--grass)"/>
      <path d="M380 740 Q470 640 520 490 L520 740 Z" fill="url(#royal-fade)"/>
    </svg>

    <div class="club-mark">
      <div class="disc"></div>
      <span>Lumaray Vellardo</span>
    </div>

    <header class="club-details">
      <div class="club-name">Lumaray <span>Vellardo</span></div>
      <address>Suite 4, 112 Via Lumaro,<br>VELLARDO, Italy 10028</address>
    </header>

    <div class="watermark" role="img" aria-label="Faint club watermark">
      <span>Lumaray<br>Vellardo</span>
    </div>

    <article class="letter-body">
      <div class="salutation">Dear Mr. Solicitor,</div>
      <p>Lorem ipsum dolor sit amet, consectetur adipiscing elit. Vestibulum nec nunc sollicitudin, dictum ligula vitae, accumsan felis. Donec at quam felis. Pellentesque feugiat condimentum adipiscing. Maecenas sit amet neque ligula. Suspendisse ut libero in justo ullamcorper porttitor et vel orci. In consequat nibh in lacinia facilisis. Interdum et malesuada fames ac ante ipsum primis in faucibus. Cras adipiscing turpis lacus, eu faucibus nibh laoreet vel. Etiam pellentesque massa eu sodales interdum, mi nisi sagittis sem, sit amet feugiat turpis erat ac arcu. Proin at tincidunt nulla, sed feugiat massa. Maecenas suscipit purus nec orci rutrum, non auctor eros vulputate. Ut nec erat mollis, placerat risus venenatis, pharetra quam. Mauris hendrerit interdum ante, nec molestie ipsum faucibus eu.</p>
      <p>Nulla nec risus non quam mollis volutpat. Suspendisse sit amet dignissim purus. Sed fringilla ipsum eu ullamcorper posuere. In odio odio, tempor eu dictum a, pulvinar eu eros. Sed suscipit id risus a rhoncus. Mauris mollis dictum libero, vel lacinia sapien ullamcorper quis. Ut nec erat mollis, placerat risus venenatis, pharetra quam. Mauris hendrerit interdum ante, nec molestie ipsum faucibus eu. Etiam ultrices sapien quis blandit ullamcorper, diam diam mollis urna, sed tempor diam nulla ut odio. Cras sollicitudin semper convallis. Sed suscipit id risus a rhoncus.</p>
      <span class="signature" role="img" aria-label="Handwritten signature"></span>
    </article>

    <ul class="contact-list">
      <li>(00) 0000 0000</li>
      <li>info@lumarayvellardo.it</li>
      <li>www.lumarayvellardo.it</li>
      <li>@lumarayvellardo</li>
      <li>Vat 00000000000</li>
      <li>Tax 00000000000</li>
    </ul>
  </main>
</body>
</html>
```